Lens Troupe Nordic Website - Photography and Films

We are looking for a design that expresses the friendly, open nature of our company Lens Troupe Nordic, yet at the same time is professional looking and functional.

Lens Troupe Nordic is a B2B focused operation that hires out multi-lingual camera crews (and equipment) throughout Germany and Europe. We also produce tv features and coporate films. Our unique selling point is that we are native English speakers who can communicate with our international clients (usually British or American) and organise the logistics of shooting in foreign countries.

For content inspiration, see our current website: http://www.lenstroupenordic.example - however we want to move away from the very simple structure of this site and move towards a layout that displays and allows for frequently updated content (e.g. in the form of a blog).

Here is an example of the kind of clean look we like:
http://www.vistaclipvault.example/gallery/home/reelsvcv.do#reel=48203716

Please keep within the following specifications:
- We wish to keep our logo (grey/white, font: Glypha) and our company colour red (#C40A0A) as they are.
- Maximum Width 960px, on a large browser-window the design should be centred
- Easily readable font sizes with good contrast
- Provide your design in PSD file format
- Our logo should be graphically displayed in the top left of the header.
- The design should allow space for a video.
- The page should have a clearly recognisable end in the form of a footer.

The following menu items need to be clearly arranged so the viewer is not overwhelmed or confused:
About
Services - Crews / Corporate Shoots / Webcasts / Production Arm / Legal Videography
Recent Productions
Blog
Testimonials
Get a Quote
Contact
Film Library
Showreel
Events
Film Location Guide - Frankfurt / Cologne / Zurich / Helsinki / Amsterdam / London / Paris / Rome / Brussels / Berlin / Munich
Updates

Reason: Hi - thanks very much for your interest in our design project.  We are extending this auction because we haven't had enough time to really focus on the desigs and provide immediate feedback to designers.  We will try to provide timely feedback and are giving you more time to make any adjustments to your designs etc.
Thanks!
Maren

Target Market(s)

Our target customers are males and females between 25 and 55 years (mostly British and American). More important than their demographic though, is their occupation - they are largely communication and design savvy individuals belonging to one of the following three categories: 1)Broadcasters (usually producers for example from the VCN or Horizon Network seeking trustworthy, affordable crews for their foreign shoots).

2) Video Production Companies (seeking a trustworthy, affordable partner company to provide the crews for their own corporate clients).

3) Corporate Communications Specialists (seeking professional producers and crews to facilitate production of company videos or filming of events).

Industry/Entity Type

Camera

Requirements
Must have
• A fresh clean appearance with good use of white space.
Should not have
• Avoid dark heavy colours and designs.
• Avoid designs that would be impractical and could potentially take a long time to load.

```html
<!DOCTYPE html>
<html lang="en">
<head>
<meta charset="utf-8">
<title>Lens Troupe Nordic – Home</title>
<link href="https://fonts.googleapis.com/css2?family=Arvo:wght@400;700&family=Open+Sans:ital,wght@0,400;0,600;1,400&display=swap" rel="stylesheet">
<style>
  :root {
    --brand-red: #c40a0a;
    --page-grey: #e2e2e2;
    --panel-white: #fbfbfb;
    --ink: #333333;
    --ink-soft: #444444;
    --rule: #c8c8c8;
    --utility-grey: #9a9a9a;
    --footer-dark: #2b2b2b;
    --white: #ffffff;
  }
  * { box-sizing: border-box; margin: 0; padding: 0; }
  html, body { width: 1200px; height: 1100px; overflow: hidden; }
  body {
    position: relative;
    background: var(--page-grey);
    font-family: "Open Sans", Arial, sans-serif;
    color: var(--ink);
  }
  a { color: inherit; text-decoration: none; }
  ul { list-style: none; }

  .top-bar {
    position: absolute; left: 0; top: 0; width: 1200px; height: 46px;
    background: var(--white); border-bottom: 1px solid #d0d0d0;
  }
  .brand {
    position: absolute; left: 123px; top: 10px; width: 282px; height: 46px;
    background: var(--brand-red); color: var(--white);
    font-family: "Arvo", Georgia, serif; font-weight: 700; font-size: 22px;
    display: flex; align-items: center; justify-content: center;
  }
  .location-guide {
    position: absolute; left: 564px; top: 14px;
    font-family: "Arvo", Georgia, serif; font-weight: 400; font-size: 14px;
    color: var(--brand-red);
  }
  .utility-links {
    position: absolute; left: 850px; top: 12px; display: flex; gap: 26px;
    font-size: 13px; color: #8a8a8a; font-weight: 600;
  }
  .utility-links a { display: flex; align-items: center; gap: 10px; }
  .search {
    position: absolute; left: 778px; top: 65px; width: 301px; height: 26px;
    background: var(--utility-grey); color: #f2f2f2; font-size: 13px;
    padding: 4px 10px; display: flex; justify-content: space-between; align-items: center;
  }

  .main-nav {
    position: absolute; left: 120px; top: 110px; width: 960px; height: 42px;
    background: var(--brand-red);
  }
  .main-nav ul { display: flex; height: 42px; padding-left: 12px; }
  .main-nav a {
    display: block; height: 42px; line-height: 42px; padding: 0 19px;
    font-family: "Arvo", Georgia, serif; font-size: 13.5px; color: var(--white);
  }
  .main-nav .current a {
    background: var(--panel-white); color: var(--brand-red);
    height: 50px; margin-top: -8px; line-height: 58px; padding: 0 26px;
  }

  .content {
    position: absolute; left: 120px; top: 152px; width: 960px; height: 753px;
    background: var(--panel-white);
  }
  .tagline {
    position: absolute; left: 0; top: 20px; width: 960px; text-align: center;
    font-family: "Arvo", Georgia, serif; font-size: 20px; font-weight: 400; color: var(--ink);
  }
  .rule { position: absolute; left: 20px; width: 920px; height: 1px; background: var(--rule); }

  .video-player {
    position: absolute; left: 38px; top: 77px; width: 438px; height: 263px;
    background: linear-gradient(#4a4a4a, #1c1c1c 70%, #0c0c0c);
  }
  .video-intro { position: absolute; left: 523px; top: 82px; width: 380px; }
  .video-intro h2 { font-weight: 400; font-size: 25px; color: var(--brand-red); margin-bottom: 2px; }
  .video-intro p { font-size: 13.5px; line-height: 24px; color: var(--ink-soft); padding-left: 4px; }

  .post-date {
    position: absolute; left: 1px; top: 392px; width: 67px; height: 57px;
    background: var(--brand-red); color: var(--white); text-align: center;
  }
  .post-date .day { display: block; font-size: 36px; line-height: 38px; }
  .post-date .month { display: block; font-size: 13px; line-height: 16px; }
  .post-title {
    position: absolute; left: 80px; top: 398px;
    font-style: italic; font-weight: 400; font-size: 30px; color: var(--ink-soft); letter-spacing: 0.5px;
  }
  .post-photo {
    position: absolute; left: 76px; top: 445px; width: 300px; height: 199px;
    background: linear-gradient(135deg, #e8e8e8, #9c9c9c 55%, #2e2e2e);
    border: 1px solid #bdbdbd;
  }
  .post-excerpt { position: absolute; left: 76px; top: 651px; width: 350px; font-size: 12.5px; line-height: 24px; }
  .read-more {
    position: absolute; left: 75px; top: 710px; width: 89px; height: 22px;
    background: var(--brand-red); color: var(--white); font-size: 12px; text-align: center; line-height: 22px;
  }

  .pitch { position: absolute; left: 508px; top: 396px; width: 425px; }
  .pitch h3 {
    width: 410px;
    font-family: "Arvo", Georgia, serif; font-weight: 400; font-size: 16px;
    line-height: 30px; color: var(--brand-red);
  }
  .pitch .cta {
    font-style: italic; color: var(--white); background: #3d3d3d; padding: 1px 5px;
    white-space: nowrap;
  }
  .pitch p { width: 415px; font-size: 12.5px; line-height: 24px; margin-top: 6px; color: var(--ink-soft); }
  .pitch ul { margin-top: 17px; padding-left: 18px; }
  .pitch li { font-size: 14px; line-height: 24px; display: flex; align-items: center; gap: 8px; }

  .site-footer {
    position: absolute; left: 121px; top: 905px; width: 960px; height: 195px;
    background: var(--footer-dark); color: var(--white);
  }
  .company-info { position: absolute; left: 24px; top: 10px; font-size: 11.5px; line-height: 24px; }
  .company-info .copyright { font-size: 14px; padding-left: 4px; }
  .footer-col { position: absolute; top: 12px; font-size: 11px; line-height: 18px; }
  .footer-col h4 { font-weight: 400; font-size: 13px; color: var(--brand-red); line-height: 18px; }
</style>
</head>
<body>
  <header class="top-bar">
    <a class="brand" href="#">Lens Troupe Nordic</a>
    <a class="location-guide" href="#">Film Location Guide</a>
    <nav class="utility-links">
      <a href="#"><svg width="24" height="22" viewBox="0 0 24 22"><rect x="1" y="5" width="15" height="15" fill="none" stroke="#999" stroke-width="2"/><path d="M9 14 L20 3 L23 6 L12 17 L8 18 Z" fill="#999"/></svg>Get a Quote</a>
      <a href="#"><svg width="22" height="22" viewBox="0 0 22 22"><path d="M3 3 C1 6 4 13 9 17 C13 20 17 21 19 19 L16 15 L13 16 C10 14 8 12 7 9 L8 6 Z" fill="#999"/></svg>Contact</a>
    </nav>
  </header>

  <form class="search"><span>search</span>
    <svg width="15" height="15" viewBox="0 0 15 15"><circle cx="6" cy="6" r="4.5" fill="none" stroke="#fff" stroke-width="2"/><path d="M9.5 9.5 L14 14" stroke="#fff" stroke-width="2.5"/></svg>
  </form>

  <nav class="main-nav">
    <ul>
      <li class="current"><a href="#">Home</a></li>
      <li><a href="#">About</a></li>
      <li><a href="#">Services</a></li>
      <li><a href="#">Recent Productions</a></li>
      <li><a href="#">Blog</a></li>
      <li><a href="#">Testimonials</a></li>
      <li><a href="#">Film Library</a></li>
      <li><a href="#">Showreel</a></li>
      <li><a href="#">Events</a></li>
    </ul>
  </nav>

  <main class="content">
    <h1 class="tagline">No job is too big, too small, too hard, too far away, or too urgent.</h1>
    <div class="rule" style="top:57px"></div>

    <div class="video-player" role="img" aria-label="Featured video player">
      <svg width="438" height="263" viewBox="0 0 438 263">
        <circle cx="218" cy="110" r="28" fill="rgba(255,255,255,0.1)" stroke="#cfcfcf" stroke-width="3"/>
        <path d="M210 97 L232 110 L210 123 Z" fill="#d8d8d8"/>
        <rect x="10" y="240" width="8" height="8" fill="#fff"/>
        <circle cx="38" cy="244" r="8" fill="#333"/><path d="M35 240 L42 244 L35 248 Z" fill="#fff"/>
        <rect x="52" y="242" width="212" height="4" rx="2" fill="#888"/>
        <circle cx="55" cy="244" r="3.5" fill="#fff"/>
        <rect x="273" y="236" width="76" height="16" fill="#111"/>
        <text x="279" y="248" font-family="Open Sans, sans-serif" font-size="10.5" fill="#e8e84a">00:00/<tspan fill="#ddd">03:06</tspan></text>
        <path d="M360 241 L364 241 L368 238 L368 250 L364 247 L360 247 Z" fill="#ddd"/>
        <rect x="372" y="242" width="36" height="4" rx="2" fill="#888"/><circle cx="390" cy="244" r="3.5" fill="#fff"/>
        <rect x="418" y="238" width="7" height="7" fill="#ddd"/>
      </svg>
    </div>

    <section class="video-intro">
      <h2>Video Title</h2>
      <p>Vel ut quas utroque placerat, kasd utinam epicuri at est, hendrerit argumentum dissentias ei nec. Te quo probatus consequuntur, id omnis audiam perfecto qui. Volumus singulis et est, fuisset invidunt convenire quo ea, omnis nostrum luptatum in eum. Ius id essent sanctus erroribus. Nam ex definiebas dissentiet, ex ubique tritani quaerendum eum. An facer insolens [...]</p>
    </section>

    <div class="rule" style="top:372px"></div>

    <article>
      <div class="post-date"><span class="day">4</span><span class="month">DEC</span></div>
      <h2 class="post-title">Latest Blog Post Title</h2>
      <div class="post-photo" role="img" aria-label="Camera operator with a professional video camera on set"></div>
      <p class="post-excerpt">Vel ut quas utroque placerat, kasd utinam epicuri at est, hendrerit argumentum dissentias ei nec. Te quo [...]</p>
      <a class="read-more" href="#">READ MORE</a>
    </article>

    <section class="pitch">
      <h3>As a producer, you’re bound to have great ideas…<br>but how do you make them a reality in a country<br>where you can’t speak the language? <span class="cta">Partner with us!</span></h3>
      <p>We meet the production demands of the growing number of English speaking TV-producers working in Europe. Our passion is film and we’ve been doing it for over 30 years. We are native English speakers so nothing gets lost in translation. We’ll catch hold of your vision, and with local know-how, we’ll make it happen.</p>
      <ul>
        <li><svg width="10" height="12" viewBox="0 0 10 12"><path d="M0 0 L10 6 L0 12 Z" fill="#c40a0a"/></svg>Crews and facilities throughout Germany and Europe</li>
        <li><svg width="10" height="12" viewBox="0 0 10 12"><path d="M0 0 L10 6 L0 12 Z" fill="#c40a0a"/></svg>PAL and NTSC Formats</li>
        <li><svg width="10" height="12" viewBox="0 0 10 12"><path d="M0 0 L10 6 L0 12 Z" fill="#c40a0a"/></svg>Flexible editing locales and transfer via FTP or SNG</li>
        <li><svg width="10" height="12" viewBox="0 0 10 12"><path d="M0 0 L10 6 L0 12 Z" fill="#c40a0a"/></svg>On call 24/7</li>
      </ul>
    </section>
  </main>

  <footer class="site-footer">
    <div class="company-info">
      <p class="copyright">Copyright Lens Troupe Nordic. All Rights Reserved</p>
      <p>c/o Halvard Films · Lindenweg 12 · 20251 Nordstadt · Germany</p>
      <p>hello@lenstroupenordic.example</p>
      <p>Tel.: +49-00-555010 · Toll free from the USA 1-800-555-0147</p>
      <p>Disclaimer</p>
    </div>
    <nav class="footer-col" style="left:529px">
      <h4>SITEMAP</h4>
      <ul><li>Home</li><li>About</li><li>Services</li><li>Recent Productions</li><li>Testimonials</li><li>Film Library</li><li>Showreel</li><li>Events</li></ul>
    </nav>
    <nav class="footer-col" style="left:681px">
      <h4>BLOG</h4>
      <ul><li>Category 1</li><li>Category 2</li><li>Category 3</li><li>Category 4</li></ul>
    </nav>
    <nav class="footer-col" style="left:806px">
      <h4>CONNECT</h4>
      <ul><li>Chirpline</li><li>Friendboard</li><li>RSS</li></ul>
    </nav>
  </footer>
</body>
</html>
```